tarnu

We are a group of companies that we want to make a triptych. we want the general information of the work we do and the information of each company with its logo

```html
<!DOCTYPE html>
<html lang="es">
<head>
<meta charset="utf-8">
<title>Tarnu · Power Team NEXA · Tríptico</title>
<link href="https://fonts.googleapis.com/css2?family=Crimson+Text&family=Ubuntu:wght@400;500&family=Ubuntu+Condensed&display=swap" rel="stylesheet">
<style>
  :root{
    --stage:#c9c9cc;
    --red:#c62320;
    --red-deep:#7a1411;
    --ink:#1c1c1e;
    --charcoal:#2b2b2d;
    --paper:#f4f4f4;
    --text:#2a2a2a;
    --white:#ffffff;
  }
  *{margin:0;padding:0;box-sizing:border-box}
  html,body{width:861px;height:1200px;overflow:hidden;background:var(--stage)}
  body{position:relative;font-family:"Ubuntu",sans-serif;color:var(--text)}

  .sheet{position:absolute;left:70px;width:727px;height:516px;overflow:hidden;background:var(--paper);box-shadow:0 10px 14px -8px rgba(0,0,0,.35)}
  .sheet--outside{top:59px}
  .sheet--inside{top:616px;height:514px}

  .panel{position:absolute;top:0;width:242px;height:100%;overflow:hidden}
  .panel--a{left:0}
  .panel--b{left:242px;width:243px}
  .panel--c{left:485px}
  .panel svg.shapes{position:absolute;inset:0;width:100%;height:100%}

  .serif{font-family:"Crimson Text",serif;font-weight:400}

  /* outside – cover side */
  .group-label{position:absolute;left:24px;top:120px;color:var(--white);font-size:14px;line-height:18px;letter-spacing:.2px}
  .partners{position:absolute;left:22px;top:222px;width:208px}
  .partner{font-family:"Ubuntu",sans-serif;font-weight:500;color:#333;display:flex;align-items:center;gap:6px;white-space:nowrap}
  .partner i{display:inline-block;width:9px;height:9px;background:var(--red)}
  .partner--lead{font-size:25px;color:#3a3a3a;background:#e4e6e8;padding:2px 6px;margin-bottom:14px;letter-spacing:-.3px}
  .partner-row{display:flex;justify-content:space-between;align-items:center;margin-bottom:18px}
  .partner--md{font-size:15px}
  .partner--lg{font-size:20px}
  .partner--wide{font-size:12px;letter-spacing:2.5px;margin-top:2px}

  .services-title{position:absolute;left:20px;top:28px;color:var(--white);font-size:16px;line-height:21px}
  .services{position:absolute;left:12px;top:150px;width:222px;list-style:none;color:var(--white);font-size:10.4px;line-height:11.3px}
  .services li{position:relative;padding-left:12px;margin-bottom:6.6px}
  .services li::before{content:"";position:absolute;left:0;top:2px;width:7px;height:7px;border-radius:50%;background:var(--white)}
  .services li::after{content:"";position:absolute;left:1.6px;top:4.1px;width:2.4px;height:2.4px;border-top:1.2px solid var(--red);border-right:1.2px solid var(--red);transform:rotate(45deg)}

  .contact{position:absolute;left:26px;top:446px;list-style:none;color:var(--white);font-size:10.6px}
  .contact li{display:flex;align-items:center;gap:9px;height:20px}
  .contact svg{width:10px;height:10px}

  .brand-title{position:absolute;left:21px;top:364px;color:var(--white);font-size:35px;line-height:36px;letter-spacing:.5px;white-space:nowrap}
  .brand-rule{position:absolute;left:21px;top:474px;width:208px;height:1px;background:rgba(255,255,255,.75)}
  .brand-sub{position:absolute;left:23px;top:483px;color:var(--white);font-size:14.5px;letter-spacing:.5px}

  /* inside */
  .col-title{position:absolute;color:var(--ink);font-size:13px;line-height:16.5px}
  .col-title::after{content:"";position:absolute;left:0;bottom:-5px;width:88px;height:1.4px;background:var(--red)}
  .col-title--dark{color:var(--white)}
  .col-title--dark::after{display:none}

  .works{position:absolute;list-style:none;color:var(--text)}
  .works li{position:relative;padding-left:5px}
  .works li::before{content:"•";position:absolute;left:0}
  .works--private{left:23px;top:53px;width:212px;font-size:7.6px;line-height:8.62px}
  .works--business{left:8px;top:183px;width:228px;font-family:"Ubuntu Condensed",sans-serif;font-size:5.9px;line-height:6.62px}

  .company-services{position:absolute;left:19px;top:186px;width:212px;list-style:none;color:var(--white);font-size:7.6px;line-height:8.5px}
  .company-services li{position:relative;padding-left:12px;margin-bottom:6.4px}
  .company-services li::before{content:"";position:absolute;left:0;top:1px;width:6px;height:6px;border-radius:50%;background:var(--red)}
</style>
</head>
<body>

<section class="sheet sheet--outside">

  <div class="panel panel--a">
    <svg class="shapes" viewBox="0 0 242 516" preserveAspectRatio="none">
      <defs>
        <linearGradient id="paperFade" x1="0" y1="0" x2="1" y2="0">
          <stop offset="0" stop-color="#f6f6f6"/><stop offset="1" stop-color="#d9d9d9"/>
        </linearGradient>
        <linearGradient id="toolsPhoto" x1="0" y1="0" x2="1" y2="1">
          <stop offset="0" stop-color="#e9b21c"/><stop offset=".45" stop-color="#e8e2d6"/><stop offset="1" stop-color="#b9bcc0"/>
        </linearGradient>
      </defs>
      <rect width="242" height="516" fill="url(#paperFade)"/>
      <rect width="242" height="150" fill="url(#toolsPhoto)" role="img" aria-label="Foto de casco amarillo, planos enrollados y cinta métrica"/>
      <polygon points="150,150 242,112 242,146 190,150" fill="#c62320"/>
      <polygon points="0,93 242,118 242,146 0,190" fill="#2b2b2d"/>
      <polygon points="0,190 242,146 242,150 0,196" fill="#1c1c1e"/>
      <polygon points="0,470 242,438 242,516 0,516" fill="#1c1c1e"/>
      <polygon points="110,468 242,430 242,452 170,470" fill="#c62320"/>
    </svg>
    <h2 class="group-label serif">GRUPO DE<br>CONSTRUCCIÓN</h2>
    <div class="partners">
      <div class="partner partner--lead">Marlo Estudio</div>
      <div class="partner-row">
        <span class="partner partner--md"><i></i>Brisa Carpintería</span>
        <span class="partner partner--md">Ontel</span>
      </div>
      <div class="partner-row">
        <span class="partner partner--lg">Corva Grupo</span>
        <span class="partner partner--lg">Vidrex</span>
      </div>
      <div class="partner partner--wide">FERRAN ARQUITECTOS</div>
    </div>
  </div>

  <div class="panel panel--b">
    <svg class="shapes" viewBox="0 0 243 516" preserveAspectRatio="none">
      <defs>
        <linearGradient id="redFade" x1="0" y1="0" x2="0" y2="1">
          <stop offset="0" stop-color="#c62320"/><stop offset="1" stop-color="#7a1411"/>
        </linearGradient>
      </defs>
      <rect width="243" height="516" fill="#1c1c1e"/>
      <polygon points="0,144 243,97 243,392 0,446" fill="url(#redFade)"/>
      <polygon points="0,140 243,93 243,97 0,144" fill="#e5e5e5"/>
    </svg>
    <h2 class="services-title serif">DISEÑO Y GESTIÓN DE<br>PROYECTOS Y OBRAS<br>PARA PARTICULARES</h2>
    <ul class="services">
      <li>Proyecto de obra nueva</li>
      <li>Proyecto de reforma y rehabilitación</li>
      <li>Proyecto de interiorismo y decoración</li>
      <li>Proyecto de cambio de uso de locales comerciales y oficinas a vivienda</li>
      <li>Proyecto de legalización de viviendas y otras construcciones</li>
      <li>Tramitación de licencia de obras ante ayuntamientos y administraciones equivalentes</li>
      <li>Dirección de obra</li>
      <li>Comercialización y valoración de inmuebles, tanto para clientes nacionales como extranjeros que busquen propiedades en España, con especial énfasis en viviendas de alto standing en zonas costeras</li>
    </ul>
    <ul class="contact">
      <li><svg viewBox="0 0 10 10"><path d="M2 1l2 2-1 1.3c.6 1.2 1.5 2.1 2.7 2.7L7 6l2 2-1.3 1.3C4.5 9 1 5.5.7 2.3z" fill="#fff"/></svg>555 019 284</li>
      <li><svg viewBox="0 0 10 10"><rect x="0.5" y="2" width="9" height="6.5" rx="1" fill="#fff"/><path d="M1 2.5l4 3 4-3" stroke="#1c1c1e" fill="none" stroke-width="1"/></svg>tarnu@teamnexa.com</li>
      <li><svg viewBox="0 0 10 10"><rect x="0.5" y="0.5" width="9" height="9" rx="1.5" fill="#fff"/><path d="M5 2a2 2 0 012 2c0 1.5-2 4-2 4S3 5.5 3 4a2 2 0 012-2z" fill="#1c1c1e"/></svg>P.O. Box Tarnu Grupo de construcción</li>
    </ul>
  </div>

  <div class="panel panel--c">
    <svg class="shapes" viewBox="0 0 242 516" preserveAspectRatio="none">
      <defs>
        <linearGradient id="siteSky" x1="0" y1="0" x2="0" y2="1">
          <stop offset="0" stop-color="#8fa6bd"/><stop offset=".55" stop-color="#b9bcc0"/><stop offset="1" stop-color="#a9744d"/>
        </linearGradient>
        <linearGradient id="redFadeC" x1="0" y1="0" x2="0" y2="1">
          <stop offset="0" stop-color="#c62320"/><stop offset="1" stop-color="#7a1411"/>
        </linearGradient>
      </defs>
      <rect width="242" height="370" fill="url(#siteSky)" role="img" aria-label="Foto de obrero con casco amarillo ante un edificio en construcción y grúas"/>
      <polygon points="0,354 242,298 242,516 0,516" fill="#1c1c1e"/>
      <polygon points="0,362 242,305 242,516 0,516" fill="url(#redFadeC)"/>
    </svg>
    <h1 class="brand-title serif">POWER<br>TEAM NEXA<br>TARNU</h1>
    <div class="brand-rule"></div>
    <p class="brand-sub">GRUPO DE CONSTRUCCIÓN</p>
  </div>
</section>

<section class="sheet sheet--inside">

  <div class="panel panel--a">
    <svg class="shapes" viewBox="0 0 242 514" preserveAspectRatio="none">
      <defs>
        <linearGradient id="redFadeA" x1="0" y1="0" x2="1" y2="0">
          <stop offset="0" stop-color="#7a1411"/><stop offset="1" stop-color="#d42a22"/>
        </linearGradient>
      </defs>
      <rect width="242" height="514" fill="#f7f7f7"/>
      <polygon points="0,478 242,448 242,514 0,514" fill="url(#redFadeA)"/>
      <polygon points="0,486 120,514 0,514" fill="#1c1c1e"/>
    </svg>
    <h2 class="col-title serif" style="left:21px;top:11px">CONSTRUCCIÓN Y OBRA<br>PARA PARTICULARES</h2>
    <ul class="works works--private">
      <li>Derribo de construcciones</li>
      <li>Excavación y movimiento de tierras</li>
      <li>Cimentaciones de viviendas</li>
      <li>Estructuras de hormigón, acero y madera para viviendas nuevas</li>
      <li>Refuerzo y reparación de estructuras de hormigón, acero y madera para rehabilitación y/o reforma de viviendas</li>
      <li>Diseño y construcción de mobiliario a medida</li>
      <li>Diseño y construcción de cocinas a medida de la marca propia</li>
      <li>Reforma y rehabilitación de cocinas y baños</li>
      <li>Albañilería tradicional de ladrillo y tabiquería en seco de yeso laminado</li>
      <li>Pintura de viviendas y aparcamientos en edificios de viviendas</li>
      <li>Pintura de protección de elementos especiales</li>
      <li>Falsos techos registrables y fijos</li>
      <li>Construcción y reforma de cubiertas, planas o inclinadas, transitables o técnicas, en viviendas y edificios de viviendas</li>
      <li>Impermeabilización y aislamiento térmico, acústico y estanco en viviendas nuevas y a rehabilitar o reformar</li>
      <li>Impermeabilización de medianeras mediante tabiques pluviales de diferentes tipos</li>
      <li>Instalación y mantenimiento de calefacción por aire y radiador</li>
      <li>Instalación y mantenimiento de climatización por aire</li>
      <li>Alicatados en cocinas y baños</li>
      <li>Chapados y revestimientos en viviendas y zonas comunes de edificios de viviendas</li>
      <li>Pavimentos de madera, cerámica y piedra en viviendas y zonas comunes de viviendas</li>
      <li>Carpintería de madera en interiores de viviendas</li>
      <li>Carpintería de aluminio en viviendas y edificios de viviendas</li>
      <li>Instalación y mantenimiento de electricidad y domótica</li>
      <li>Instalación y mantenimiento de sistemas de alumbrado, tanto en interiores como en exteriores</li>
      <li>Instalación y mantenimiento de alumbrado de emergencia en zonas comunes de edificios de viviendas</li>
      <li>Instalación y mantenimiento de instalación de fontanería y saneamiento</li>
      <li>Instalación de ascensores especiales para viviendas</li>
      <li>Instalación y mantenimiento de instalaciones de protección contra incendios en aparcamientos de viviendas unifamiliares, aparcamientos de edificios de viviendas y zonas comunes de edificios de viviendas</li>
    </ul>
  </div>

  <div class="panel panel--b">
    <svg class="shapes" viewBox="0 0 243 514" preserveAspectRatio="none">
      <defs>
        <linearGradient id="cityPlans" x1="0" y1="0" x2="0" y2="1">
          <stop offset="0" stop-color="#b08a6a"/><stop offset=".5" stop-color="#d9d4cc"/><stop offset="1" stop-color="#eeeeee"/>
        </linearGradient>
        <linearGradient id="cityFaint" x1="0" y1="0" x2="0" y2="1">
          <stop offset="0" stop-color="#2b2b2d"/><stop offset="1" stop-color="#6b6b6e"/>
        </linearGradient>
      </defs>
      <rect width="243" height="514" fill="#1c1c1e"/>
      <polygon points="0,0 243,0 243,128 0,104" fill="url(#cityPlans)" role="img" aria-label="Foto de ciudad con edificios y planos enrollados"/>
      <polygon points="0,450 243,430 243,514 0,514" fill="url(#cityFaint)" role="img" aria-label="Foto tenue de edificios en construcción"/>
    </svg>
    <h2 class="col-title col-title--dark serif" style="left:17px;top:145px;font-size:12.4px;line-height:16px">DISEÑO Y GESTIÓN DE PROYECTOS Y<br>OBRAS PARA EMPRESAS Y NEGOCIOS</h2>
    <ul class="company-services">
      <li>Proyecto de obra nueva</li>
      <li>Proyecto de reforma y rehabilitación</li>
      <li>Proyecto de interiorismo y decoración de hoteles, locales comerciales, oficinas y edificios públicos en general</li>
      <li>Estudio de viabilidad de promociones inmobiliarias</li>
      <li>Búsqueda de terrenos y edificios para promociones inmobiliarias, gestión patrimonial y grupos inversores</li>
      <li>Búsqueda de compradores e inversores para los inmuebles de nuestros clientes</li>
      <li>Proyecto de urbanización de terrenos ubicados en zonas afectadas por planes parciales</li>
      <li>Proyecto de cambio de uso de edificios construidos, ya sean hoteles, viviendas, locales, oficinas, al uso que el cliente solicite, previa consulta con las administraciones competentes para validar la viabilidad del proceso</li>
      <li>Tramitación de licencia de obras ante ayuntamientos y administraciones equivalentes</li>
      <li>Dirección de obra</li>
      <li>Comercialización y valoración de inmuebles, tanto para clientes nacionales como extranjeros que busquen propiedades en España</li>
    </ul>
  </div>

  <div class="panel panel--c">
    <svg class="shapes" viewBox="0 0 242 514" preserveAspectRatio="none">
      <defs>
        <linearGradient id="helmetPlans" x1="0" y1="0" x2="1" y2="1">
          <stop offset="0" stop-color="#c9a27a"/><stop offset=".55" stop-color="#e9b21c"/><stop offset="1" stop-color="#e8e6e2"/>
        </linearGradient>
      </defs>
      <rect width="242" height="514" fill="#f5f5f5"/>
      <polygon points="0,0 242,0 242,150 0,128" fill="url(#helmetPlans)" role="img" aria-label="Foto de casco amarillo sobre planos enrollados con ciudad al fondo"/>
    </svg>
    <h2 class="col-title serif" style="left:8px;top:144px;font-size:12.6px">CONSTRUCCIÓN Y OBRA PARA<br>EMPRESAS Y NEGOCIOS</h2>
    <ul class="works works--business">
      <li>Derribo de construcciones</li>
      <li>Excavación y movimiento de tierras</li>
      <li>Cimentaciones de edificios</li>
      <li>Estructuras de hormigón, acero y madera</li>
      <li>Refuerzo, reparación y modificación de estructuras de hormigón, acero y madera para rehabilitación y/o reforma de edificios</li>
      <li>Diseño y construcción de mobiliario a medida para locales comerciales, oficinas, hoteles y edificios destinados al sector terciario en general</li>
      <li>Diseño y construcción de cocinas a medida de la marca propia</li>
      <li>Diseño, construcción y mantenimiento de cocinas industriales a medida para hoteles, restaurantes, cafeterías, escuelas, hospitales y cualquier establecimiento público que necesite este tipo de servicio, con equipamiento y maquinaria adecuada a sus requerimientos</li>
      <li>Asesoramiento sobre las mejores soluciones de eficiencia energética en el equipamiento de locales comerciales, hoteles y toda clase de edificios públicos que precisen de una mejora en su consumo de energía</li>
      <li>Reforma y rehabilitación de cocinas y baños en todo tipo de edificios públicos</li>
      <li>Albañilería tradicional de ladrillo y tabiquería en seco de yeso laminado, ya sea estándar o con requerimientos acústicos y/o de protección al fuego especiales</li>
      <li>Pintura de viviendas y aparcamientos, aplicando en cada caso el producto más adecuado a las necesidades y las exigencias de su uso</li>
      <li>Pintura de protección de elementos especiales</li>
      <li>Falsos techos registrables y fijos</li>
      <li>Construcción y reforma de cubiertas, tanto transitables como técnicas</li>
      <li>Impermeabilización y aislamiento térmico, acústico y estanco</li>
      <li>Impermeabilización de elementos especiales de exterior, en especial paredes medianeras</li>
      <li>Instalación y mantenimiento de climatización. Además de los métodos tradicionales, como la climatización por aire, por radiadores o convectores, somos expertos en aerotermia, geotermia y energía solar, así como el tratamiento del aire en entornos que requieran de una calidad especial en este aspecto</li>
      <li>Alicatados en cocinas y baños</li>
      <li>Chapados y revestimientos de paredes y fachadas</li>
      <li>Pavimentos de madera, cerámica y piedra, así como pavimentos técnicos</li>
      <li>Carpintería de madera en interiores</li>
      <li>Recuperación de elementos interiores de madera</li>
      <li>Carpintería de aluminio</li>
      <li>Instalación y mantenimiento de electricidad y domótica</li>
      <li>Instalación y mantenimiento de sistemas de alumbrado, tanto en interiores como en exteriores</li>
      <li>Instalación y mantenimiento de alumbrado de emergencia</li>
      <li>Instalación y mantenimiento de instalación de fontanería y saneamiento</li>
      <li>Instalación de ascensores</li>
      <li>Instalación y mantenimiento de instalaciones de protección especializada contra incendios mediante agua, gases inertes, sistemas especiales para cocinas industriales, columna seca, depósitos de agua, señalización, puertas cortafuegos, telas ignífugas o sellado de pasos de instalaciones</li>
    </ul>
  </div>
</section>

</body>
</html>
```